WardPeak landing page

The existing website at www.wardpeak-example.com needs updating. I've attached some marketing material for the color scheme to be used and potential content. The tagline should be "Real-Time Operational Intelligence." I want the landing page to be in 3 categories in this order and features within each category. Plenty of images are preferred and wording can be modified.
Wardpeak Command Centre
- Live Incident tracking and reporting with escalation on critical incidents if necessary
- Geofence Monitoring to ensure guards at the right location at the right time.
- Smart scheduling to ensure the correct training and certifications are assigned to the appropriate guard required.
- Camera compatibility to capture live and historical video for incident reporting
WardPeak Back Office Administration
- Automate Police report filing using data from submitted incidents when required.
- Track all required KPIs on a per site basis such as vehicle inspections, patrol tour details, etc
- Payroll and Invoicing using smart shift reports
- Create and manage client sites with configurable geofencing
WardPeak App
- Guard can see all site details and instructions when logging onto shift
- Ability to view all incidents that have occured at that particular site over the last 'x' days. Understand what has been happening and when.
- Report incidents with all relevant information including photo and video
- Recieve alerts when repeat offences are occuring within a configurable vicinity.

Target Market(s)

Retailers and guard companies

Coding

Coded - Design and coding required

Number of Pages Required

1 page

Requirements
Nice to have
• Use the look and feel of the logo in the design

```html
<!DOCTYPE html>
<html lang="en">
<head>
<meta charset="utf-8">
<title>WardPeak – Real-Time Operational Intelligence</title>
<link href="https://fonts.googleapis.com/css2?family=Anton&family=Space+Grotesk:wght@400;500;600;700&display=swap" rel="stylesheet">
<style>
:root{
  --navy:#0d2f52;
  --navy-dark:#0a1f38;
  --blue:#2a8fdc;
  --sky:#2ba4e2;
  --ice:#e9f6fd;
  --ice-deep:#d3edf9;
  --ink:#1d2b3a;
  --line:#d6dde5;
  --white:#ffffff;
}
*{box-sizing:border-box;margin:0;padding:0}
html,body{width:1200px;height:3188px;overflow:hidden}
body{position:relative;background:var(--white);font-family:"Space Grotesk",sans-serif;color:var(--ink)}
.abs{position:absolute}

.site-header{position:absolute;left:0;top:0;width:1200px;height:62px;background:var(--white);z-index:3}
.brand{position:absolute;left:155px;top:14px;display:flex;align-items:center;gap:8px}
.brand-dot{width:30px;height:30px;border-radius:50%;background:var(--navy)}
.brand-name{font-weight:700;font-size:25px;color:var(--navy);letter-spacing:-.3px}
.btn{position:absolute;display:flex;align-items:center;justify-content:center;font-weight:600;border-radius:3px;text-decoration:none}
.btn-navy{background:var(--navy);color:var(--white)}
.btn-white{background:var(--white);color:var(--navy)}
.nav-demo{left:847px;top:17px;width:115px;height:29px;font-size:12.5px}
.nav-login{left:976px;top:17px;width:67px;height:29px;font-size:12.5px}

.hero-shape{position:absolute;left:0;top:0;width:1200px;height:640px;z-index:1}
.hero-copy{position:absolute;left:155px;top:173px;z-index:2;color:var(--white)}
.hero-title{font-family:"Anton",sans-serif;font-size:52px;line-height:50px;color:var(--blue);text-transform:uppercase;font-weight:400;letter-spacing:-.2px}
.hero-sub{margin-top:23px;font-size:16.5px;font-weight:700}
.hero-note{margin-top:3px;font-size:11px}
.hero-cta{left:0;top:184px;width:256px;height:37px;font-size:14px;font-weight:700}

.section-title{font-weight:700;color:var(--navy);letter-spacing:-.3px}
.section-title .accent{color:var(--blue)}
.center{text-align:center;left:0;width:1200px}

.feature{position:absolute;display:flex;align-items:center;gap:12px}
.feature-shield{width:74px;height:82px;flex:none}
.feature-label{font-weight:700;font-size:14.5px;line-height:16px;color:var(--navy)}

.band{position:absolute;left:0;width:1200px}
.band-ice{background:var(--ice)}
.band-sky{background:var(--ice-deep)}
.photo{position:absolute}
.split-title{position:absolute;font-size:32px;line-height:37px;white-space:nowrap}
.bullets{position:absolute;list-style:none;font-size:12.5px;line-height:16px;color:var(--ink)}
.bullets li{position:relative;padding-left:19px;margin-bottom:12px}
.bullets li::before{content:"";position:absolute;left:0;top:2px;width:11px;height:11px;border-radius:50%;background:var(--sky)}
.bullets li::after{content:"";position:absolute;left:3px;top:5.5px;width:3px;height:3px;border-right:1.5px solid var(--white);border-top:1.5px solid var(--white);transform:rotate(45deg)}
.contact{width:110px;height:30px;font-size:12px}
.screen{position:absolute;border-radius:6px;border:4px solid var(--white);box-shadow:0 8px 24px rgba(10,31,56,.25)}

.field{position:absolute;border:1px solid var(--line);background:var(--white);font-size:11px;color:#9aa5b1;padding:0 12px;display:flex;align-items:center}
.field-area{align-items:flex-start;padding-top:12px}
.submit{left:562px;top:2756px;width:76px;height:29px;font-size:12px}

.cta-shape{position:absolute;left:0;top:2850px;width:1200px;height:301px}
.cta-title{position:absolute;top:2956px;font-weight:700;font-size:24px;line-height:25px;color:var(--blue)}
.cta-text{position:absolute;top:3025px;font-size:12px;line-height:15px;color:var(--white)}
.cta-btn{left:532px;top:3074px;width:136px;height:28px;font-size:12px;font-weight:700}

.site-footer{position:absolute;left:0;top:3151px;width:1200px;height:37px;background:var(--sky);color:var(--white);font-size:11px}
.site-footer p{position:absolute;left:155px;top:12px}
.social{position:absolute;top:8px;display:flex;gap:14px;right:155px}
.social span{width:20px;height:20px;border-radius:50%;background:var(--navy-dark);display:block}
</style>
</head>
<body>

<header class="site-header">
  <div class="brand"><span class="brand-dot"></span><span class="brand-name">WardPeak</span></div>
  <a class="btn btn-navy nav-demo">Request Demo</a>
  <a class="btn btn-navy nav-login">Login</a>
</header>

<svg class="hero-shape" viewBox="0 0 1200 640" role="img" aria-label="Photo of a uniformed security guard standing in a dark lobby">
  <defs>
    <linearGradient id="heroFill" x1="0" y1="0" x2="1" y2="1">
      <stop offset="0" stop-color="#0c2a4d"/>
      <stop offset=".55" stop-color="#123a63"/>
      <stop offset="1" stop-color="#0a1c33"/>
    </linearGradient>
    <linearGradient id="stripe" x1="0" y1="0" x2="1" y2="0">
      <stop offset="0" stop-color="#2a8fdc" stop-opacity="0"/>
      <stop offset=".3" stop-color="#2a8fdc"/>
      <stop offset=".7" stop-color="#2a8fdc"/>
      <stop offset="1" stop-color="#2a8fdc" stop-opacity="0"/>
    </linearGradient>
  </defs>
  <path d="M130 490 L560 617 Q600 629 640 617 L1070 490" fill="none" stroke="url(#stripe)" stroke-width="7"/>
  <path d="M0 62 H1200 V380 Q1200 450 1130 470 L640 606 Q600 618 560 606 L70 470 Q0 450 0 380 Z" fill="url(#heroFill)"/>
</svg>
<div class="hero-copy">
  <h1 class="hero-title">Real-Time Operational<br>Intelligence</h1>
  <p class="hero-sub">Advanced Security Solutions &amp; Workforce Management</p>
  <p class="hero-note">Protecting People, Assets, And Operations With Real-Time Intelligence.</p>
  <a class="btn btn-white hero-cta">Discover the Future of Security</a>
</div>

<h2 class="abs center section-title" style="top:686px;font-size:34px">WorkForce <span class="accent">Optimization</span></h2>
<svg class="abs" style="left:520px;top:732px" width="160" height="16" viewBox="0 0 160 16" aria-hidden="true">
  <line x1="0" y1="8" x2="66" y2="8" stroke="#c9d3dd"/><line x1="94" y1="8" x2="160" y2="8" stroke="#c9d3dd"/>
  <rect x="68" y="3" width="13" height="10" rx="5" fill="none" stroke="#0d2f52" stroke-width="2"/>
  <rect x="79" y="3" width="13" height="10" rx="5" fill="none" stroke="#2a8fdc" stroke-width="2"/>
</svg>

<svg width="0" height="0" style="position:absolute">
  <defs>
    <filter id="soft" x="-30%" y="-30%" width="160%" height="160%"><feDropShadow dx="0" dy="3" stdDeviation="4" flood-color="#0d2f52" flood-opacity=".15"/></filter>
    <symbol id="shield" viewBox="0 0 74 82"><path d="M37 4 L66 14 V42 Q66 66 37 78 Q8 66 8 42 V14 Z" fill="#fff" filter="url(#soft)"/></symbol>
  </defs>
</svg>

<div class="feature" style="left:198px;top:777px">
  <svg class="feature-shield" viewBox="0 0 74 82"><use href="#shield"/><g fill="none" stroke="#2a8fdc" stroke-width="2"><rect x="22" y="28" width="30" height="21" rx="2"/><line x1="30" y1="55" x2="44" y2="55"/><line x1="29" y1="44" x2="29" y2="38"/><line x1="35" y1="44" x2="35" y2="34"/><line x1="41" y1="44" x2="41" y2="36"/><line x1="47" y1="44" x2="47" y2="40"/></g></svg>
  <span class="feature-label">Geofence<br>Monitoring</span>
</div>
<div class="feature" style="left:495px;top:777px">
  <svg class="feature-shield" viewBox="0 0 74 82"><use href="#shield"/><g fill="none" stroke="#2a8fdc" stroke-width="2"><rect x="24" y="26" width="26" height="30" rx="2"/><polyline points="28,48 34,40 39,45 46,34"/><circle cx="30" cy="32" r="2"/></g></svg>
  <span class="feature-label">Live Incident<br>Reporting</span>
</div>
<div class="feature" style="left:772px;top:777px">
  <svg class="feature-shield" viewBox="0 0 74 82"><use href="#shield"/><g fill="none" stroke="#2a8fdc" stroke-width="2"><path d="M44 26 a6 6 0 0 1 6 6 c0 5 -6 11 -6 11 c0 0 -6 -6 -6 -11 a6 6 0 0 1 6 -6z"/><circle cx="30" cy="48" r="4"/><path d="M34 48 H46 Q50 48 48 44"/></g></svg>
  <span class="feature-label">Automated KPI<br>Tracking</span>
</div>
<div class="feature" style="left:198px;top:896px">
  <svg class="feature-shield" viewBox="0 0 74 82"><use href="#shield"/><g fill="none" stroke="#2a8fdc" stroke-width="2"><rect x="23" y="26" width="22" height="28" rx="2"/><line x1="28" y1="33" x2="40" y2="33"/><line x1="28" y1="39" x2="38" y2="39"/><path d="M44 40 L52 43 V48 Q52 54 44 57 Q36 54 36 48 V43 Z"/></g></svg>
  <span class="feature-label">Police Reporting<br>Integration</span>
</div>
<div class="feature" style="left:495px;top:896px">
  <svg class="feature-shield" viewBox="0 0 74 82"><use href="#shield"/><g fill="none" stroke="#2a8fdc" stroke-width="2"><rect x="22" y="29" width="28" height="24" rx="2"/><line x1="22" y1="36" x2="50" y2="36"/><line x1="28" y1="26" x2="28" y2="31"/><line x1="44" y1="26" x2="44" y2="31"/><circle cx="48" cy="50" r="6" fill="#fff"/></g></svg>
  <span class="feature-label">Smart Scheduling<br>w/payroll</span>
</div>
<div class="feature" style="left:772px;top:896px">
  <svg class="feature-shield" viewBox="0 0 74 82"><use href="#shield"/><g fill="none" stroke="#2a8fdc" stroke-width="2"><circle cx="37" cy="41" r="13"/><circle cx="37" cy="41" r="5"/><line x1="37" y1="28" x2="40" y2="36"/><line x1="50" y1="41" x2="42" y2="42"/><line x1="37" y1="54" x2="34" y2="46"/><line x1="24" y1="41" x2="32" y2="40"/></g></svg>
  <span class="feature-label">Camera<br>compatibility</span>
</div>

<!-- 1. command centre -->
<section class="band band-ice" style="top:1066px;height:448px"></section>
<div class="photo" style="left:819px;top:1066px;width:381px;height:448px;background:linear-gradient(135deg,#0b2240,#1b5a8c 55%,#0a1a30)" role="img" aria-label="Photo of a security officer watching monitoring screens"></div>
<div class="screen" style="left:721px;top:1167px;width:279px;height:252px;background:linear-gradient(160deg,#f4f7fa,#dde6ee)" role="img" aria-label="Web dashboard showing guards on shift, incidents and a site map"></div>
<h2 class="section-title split-title" style="left:156px;top:1136px">Wardpeak<br>Command <span class="accent">Centre</span></h2>
<svg class="abs" style="left:222px;top:1210px" width="28" height="12" viewBox="0 0 28 12" aria-hidden="true"><rect x="1" y="1" width="13" height="10" rx="5" fill="none" stroke="#0d2f52" stroke-width="2"/><rect x="13" y="1" width="13" height="10" rx="5" fill="none" stroke="#2a8fdc" stroke-width="2"/></svg>
<ul class="bullets" style="left:156px;top:1237px;width:520px">
  <li>Live Incident tracking and reporting with escalation on<br>critical incidents if necessary</li>
  <li>Geofence Monitoring to ensure guards at the right location at the right time.</li>
  <li>Smart scheduling to ensure the correct training and certifications are assigned to the appropriate guard required.</li>
  <li>Camera compatibility to capture live and historical video<br>for incident reporting</li>
</ul>
<a class="btn btn-navy contact" style="left:156px;top:1409px">Contact Now</a>

<!-- 2. back office administration -->
<section class="band band-sky" style="top:1514px;height:448px"></section>
<div class="photo" style="left:0;top:1514px;width:381px;height:448px;background:linear-gradient(150deg,#0f2a4a,#4a6f93 60%,#1a2c40)" role="img" aria-label="Photo of an office administrator working at a desk"></div>
<div class="photo" style="left:190px;top:1598px;width:314px;height:284px;border-radius:10px 10px 4px 4px;background:linear-gradient(90deg,#16345a 0 14%,#f2f5f8 14%);border:6px solid #1b1f26;border-bottom-width:14px" role="img" aria-label="Laptop showing the police reports form in the admin portal"></div>
<h2 class="section-title split-title" style="left:536px;top:1600px">WardPeak Back<br>Office <span class="accent">Administration</span></h2>
<svg class="abs" style="left:602px;top:1674px" width="28" height="12" viewBox="0 0 28 12" aria-hidden="true"><rect x="1" y="1" width="13" height="10" rx="5" fill="none" stroke="#0d2f52" stroke-width="2"/><rect x="13" y="1" width="13" height="10" rx="5" fill="none" stroke="#2a8fdc" stroke-width="2"/></svg>
<ul class="bullets" style="left:536px;top:1701px;width:540px">
  <li>Automate Police report filing using data from submitted incidents when required.</li>
  <li>Track all required KPIs on a per site basis such as vehicle inspections, patrol tour<br>details, etc</li>
  <li>Payroll and Invoicing using smart shift reports</li>
  <li>Create and manage client sites with configurable geofencing</li>
</ul>
<a class="btn btn-navy contact" style="left:536px;top:1846px">Contact Now</a>

<!-- 3. app -->
<section class="band band-ice" style="top:1962px;height:448px"></section>
<div class="photo" style="left:819px;top:1962px;width:381px;height:448px;background:radial-gradient(circle at 60% 45%,#0d6a78,#0a1a24 65%)" role="img" aria-label="Photo of hands holding a phone with a glowing lock shield"></div>
<div class="photo" style="left:700px;top:2046px;width:309px;height:280px;border-radius:18px;background:linear-gradient(180deg,#f2f5f8,#d9e2ea);box-shadow:0 10px 24px rgba(0,0,0,.3)" role="img" aria-label="Three phone screens of the guard app: incident reporting, shift timeline and SOS"></div>
<h2 class="section-title split-title" style="left:156px;top:2078px">WardPeak <span class="accent">App</span></h2>
<svg class="abs" style="left:222px;top:2116px" width="28" height="12" viewBox="0 0 28 12" aria-hidden="true"><rect x="1" y="1" width="13" height="10" rx="5" fill="none" stroke="#0d2f52" stroke-width="2"/><rect x="13" y="1" width="13" height="10" rx="5" fill="none" stroke="#2a8fdc" stroke-width="2"/></svg>
<ul class="bullets" style="left:156px;top:2143px;width:530px">
  <li>Guard can see all site details and instructions when logging onto shift</li>
  <li>Ability to view all incidents that have occured at that particular site over the last 'x'<br>days. Understand what has been happening and when.</li>
  <li>Report incidents with all relevant information including photo and video</li>
  <li>Recieve alerts when repeat offences are occuring within a configurable vicinity.</li>
</ul>
<a class="btn btn-navy contact" style="left:156px;top:2288px">Contact Now</a>

<!-- inquiry -->
<h2 class="abs center section-title" style="top:2484px;font-size:32px">Quick <span class="accent">Inquiry</span></h2>
<svg class="abs" style="left:516px;top:2523px" width="160" height="14" viewBox="0 0 160 14" aria-hidden="true">
  <line x1="0" y1="7" x2="66" y2="7" stroke="#c9d3dd"/><line x1="94" y1="7" x2="160" y2="7" stroke="#c9d3dd"/>
  <rect x="68" y="2" width="13" height="10" rx="5" fill="none" stroke="#0d2f52" stroke-width="2"/>
  <rect x="79" y="2" width="13" height="10" rx="5" fill="none" stroke="#2a8fdc" stroke-width="2"/>
</svg>
<div class="field" style="left:325px;top:2556px;width:268px;height:33px">First Name</div>
<div class="field" style="left:606px;top:2556px;width:269px;height:33px">Last Name</div>
<div class="field" style="left:325px;top:2605px;width:268px;height:33px">Email</div>
<div class="field" style="left:606px;top:2605px;width:269px;height:33px">Phone</div>
<div class="field field-area" style="left:325px;top:2655px;width:550px;height:78px">How Can We Help?</div>
<a class="btn btn-navy submit">Submit</a>

<svg class="cta-shape" viewBox="0 0 1200 301" role="img" aria-label="Dark photo of a security team as backdrop">
  <defs>
    <linearGradient id="ctaFill" x1="0" y1="0" x2="0" y2="1">
      <stop offset="0" stop-color="#163c66"/><stop offset="1" stop-color="#0a1b31"/>
    </linearGradient>
    <linearGradient id="ctaStripe" x1="0" y1="0" x2="1" y2="0">
      <stop offset="0" stop-color="#2a8fdc" stop-opacity="0"/><stop offset=".3" stop-color="#2a8fdc"/>
      <stop offset=".7" stop-color="#2a8fdc"/><stop offset="1" stop-color="#2a8fdc" stop-opacity="0"/>
    </linearGradient>
  </defs>
  <path d="M130 132 L560 12 Q600 0 640 12 L1070 132" fill="none" stroke="url(#ctaStripe)" stroke-width="7"/>
  <path d="M0 301 V210 Q0 160 60 146 L560 22 Q600 12 640 22 L1140 146 Q1200 160 1200 210 V301 Z" fill="url(#ctaFill)"/>
</svg>
<h2 class="cta-title center">Ready to Revolutionize<br>Your Security Operations?</h2>
<p class="cta-text center">Join industry leaders who trust WardPeak to simplify security management, enhance<br>operational efficiency, and ensure comprehensive protection.</p>
<a class="btn btn-white cta-btn">Get Started Today</a>

<footer class="site-footer">
  <p>© 2026 Ward Peak. All Rights Reserved.</p>
  <div class="social" aria-label="Social links"><span></span><span></span><span></span></div>
</footer>

</body>
</html>
```